Larkmoor Web Design Project

I need the front page and an internal page designed for this client's website. The logo is attached. Obviously the colors have to go with and/or work with the logo colors. I also attached a very rough brochure layout to help you see the direction we're going in with print materials. The rough site map is also attached. I see a slider on the homepage, the art for which I may come back to you to create. This clinic is in a very high end Dallas neighborhood. The hook is that it's a primary care and urgent facility with convenient hours.

I don't know how much this impacts your design, but this will be a Wordpress site and I'm using a framework called PageLines (framevault.example). If PageLines proves to be inflexible, I'll have to get a template that allows me to execute your design.

This site (http://sundaleclinicgroup.example) has the type and quality of content I will eventually have on the Larkmoor site.
Updates

I just revised the brief for this project. I added the site map and added details to the overview and the "Must Have" section. Thank you for revisiting the brief. 

Reason: Christmas was a bad time to end it.

Target Market(s)

Women 25-54 with children living at home, income over $150k/year

Industry/Entity Type

Clinic

Requirements
Must have
• Masthead incorporating the logo
Followed by the primary nav
Slider on the home page below that
Dual nav - 1 with the nav in the attached site map
2 secondary nav with areas of healthcare
There will three blocks under the nav
1. It's about time (with a small blurb less than 50 words.
2. It's about choices (with small blurb)
3. It's about you (with small blurb)
Three footer blocks
patient check in link on every page
"No appointment? No problem" icon on every page

```html
<!DOCTYPE html>
<html lang="en">
<head>
<meta charset="utf-8">
<title>Larkmoor Medical – Immediate Family and Personal Care</title>
<link href="https://fonts.googleapis.com/css2?family=Arimo:ital,wght@0,400;0,700;1,400&family=Roboto+Condensed:wght@400;700&display=swap" rel="stylesheet">
<style>
:root{
  --blue:#1e5fa3;
  --green:#1aae57;
  --green-text:#23a84f;
  --text:#333;
  --rule:#8c8c8c;
  --panel:#ffffff;
  --grey-head:#d3d3d3;
  --sky-top:#22599f;
  --sky-mid:#5f8fcb;
  --cloud:#f3f6fa;
}
*{box-sizing:border-box;margin:0;padding:0}
html,body{width:1077px;height:1200px;overflow:hidden}
body{
  position:relative;
  font-family:"Arimo",Arial,sans-serif;
  color:var(--text);
  background:
    radial-gradient(ellipse 420px 380px at 0px 560px,var(--cloud) 0%,rgba(243,246,250,.85) 45%,rgba(243,246,250,0) 100%),
    radial-gradient(ellipse 300px 420px at 1077px 600px,var(--cloud) 0%,rgba(243,246,250,.8) 45%,rgba(243,246,250,0) 100%),
    linear-gradient(180deg,var(--sky-top) 0%,var(--sky-mid) 30%,#dfe8f3 65%,#f2f4f7 100%);
}
a{color:inherit;text-decoration:none}
.abs{position:absolute}

.top-links{top:11px;right:92px;font-size:12px;font-weight:700;color:#fff;word-spacing:5px}

.page{left:93px;top:35px;width:891px;height:843px;background:var(--panel);border:1px solid #c9c9c9;border-radius:3px}
.brand-name{left:111px;top:62px;font-size:34px;font-weight:700;color:var(--blue);line-height:1}
.brand-tag{left:112px;top:99px;font-size:12px;color:#555}
.phone{right:112px;top:60px;font-size:29px;font-weight:700;color:var(--blue)}
.address{right:112px;top:94px;font-size:14px;color:var(--green-text)}

.main-nav{left:93px;top:133px;width:891px;height:37px;background:var(--green);color:#fff;font-size:15px;font-weight:700}
.main-nav a{position:absolute;top:10px}

.side-head{left:111px;width:200px;height:33px;background:var(--grey-head);border-bottom:2px solid #9a9a9a;
  font-family:"Roboto Condensed",sans-serif;font-weight:700;font-size:17px;color:#444;padding:8px 10px 0}
.care-list{left:111px;top:222px;width:200px;list-style:none}
.care-list li{height:33.5px;border-bottom:1px solid var(--rule);display:flex;justify-content:space-between;align-items:center;padding:2px 8px 0 10px;font-size:14px;color:#333}

.field{left:111px;width:200px;border:1px solid #888;font-size:12.5px;color:#999;padding:8px 9px}
.submit{left:111px;top:804px;width:88px;height:37px;background:var(--green);color:#fff;font-weight:700;font-size:16px;display:flex;align-items:center;justify-content:center}

.slider{left:334px;top:189px;width:632px;height:266px;background:linear-gradient(135deg,#c98f6e 0%,#e8c3a2 35%,#d7a27f 60%,#b77657 100%)}
.slider-caption{left:334px;top:421px;width:632px;height:34px;background:rgba(40,40,40,.72);color:#fff;font-size:19px;text-align:center;line-height:34px}

.welcome{left:334px;top:488px;font-size:24px;font-weight:700;color:var(--blue)}
.intro{left:334px;top:524px;width:420px;font-size:12.6px;line-height:19.5px;color:#333}
.video{left:761px;top:528px;width:205px;height:115px;background:linear-gradient(90deg,#e9e3dc 0%,#d8c4b4 40%,#f1ede8 70%,#d9cfc4 100%)}
.play{left:844px;top:573px;width:42px;height:28px;background:rgba(70,70,70,.8);border-radius:3px}

.pillar{top:680px;width:205px;height:161px;border:1px solid #9a9a9a;border-radius:4px;background:linear-gradient(180deg,#fff 55%,#ececec 100%);padding:0 9px}
.pillar h3{font-family:"Roboto Condensed",sans-serif;font-weight:700;font-size:17px;color:#333;text-align:center;margin-top:14px;word-spacing:3px}
.pillar p{font-style:italic;font-size:12.3px;line-height:15.8px;color:#333;margin-top:8px;letter-spacing:.4px}
.more{display:block;text-align:right;font-size:10.5px;font-weight:700;color:var(--green-text);margin-top:9px}

.side-tab{left:985px;width:28px;background:var(--blue);border-radius:0 3px 3px 0;color:#fff;font-size:11px;font-weight:700;writing-mode:vertical-rl;display:flex;align-items:center;padding-top:8px;gap:10px}
.side-tab svg{writing-mode:horizontal-tb}

.footer-panel{left:93px;top:898px;width:891px;height:240px;border:1px solid #9a9a9a;border-radius:4px;background:linear-gradient(180deg,#fff 40%,#ececec 100%)}
.foot-head{top:919px;font-family:"Roboto Condensed",sans-serif;font-weight:700;font-size:19px;color:var(--blue)}
.map{left:111px;top:949px;width:254px;height:97px;background:linear-gradient(135deg,#e9e6d6 0%,#f1e78a 45%,#e4e0cf 100%)}
.hours-photo{left:412px;top:949px;width:253px;height:97px;background:linear-gradient(90deg,#9fb57b 0%,#dfe6cf 45%,#e8cbb3 70%,#f4f4f2 100%)}
.foot-text{font-size:14px;line-height:16px;color:#333}
.foot-link{font-size:10.5px;font-weight:700;color:var(--green-text);text-align:right;line-height:14px}
.news{left:712px;top:944px;list-style:none;font-size:14px;line-height:23.2px}
.news li::before{content:"• "}
.social{top:1085px;width:30px;height:30px;border-radius:3px}

.bottom-nav{left:0;top:1156px;width:1077px;text-align:center;font-size:12.5px;color:#777;word-spacing:6px}
.copyright{left:0;top:1175px;width:1077px;text-align:center;font-size:10px;font-style:italic;color:#888}
</style>
</head>
<body>

<nav class="abs top-links">— <a>Register</a> — <a>Login</a> — <a>Blog</a> —</nav>

<div class="abs page"></div>

<header>
  <div class="abs brand-name">Larkmoor Medical</div>
  <div class="abs brand-tag">Immediate Family and Personal Care</div>
  <div class="abs phone">(214) 555 0182</div>
  <div class="abs address">4120 Larkmoor Ave Ste 180, Dallas, TX 75225</div>
</header>

<nav class="abs main-nav">
  <a style="left:19px">Home</a><a style="left:97px">About Us</a><a style="left:192px">Services</a>
  <a style="left:282px">Staff</a><a style="left:344px">Insurance</a><a style="left:442px">Videos</a>
  <a style="left:520px">Contact Us</a>
</nav>

<aside>
  <div class="abs side-head" style="top:189px">HEALTHCARE</div>
  <ul class="abs care-list">
    <li>Immediate Care<span>&gt;</span></li>
    <li>Allergies<span>&gt;</span></li>
    <li>Primary Care<span>&gt;</span></li>
    <li>Women's Health<span>&gt;</span></li>
    <li>Medical Spa Treatments<span>&gt;</span></li>
    <li>Men's Health<span>&gt;</span></li>
    <li>Weight Loss<span>&gt;</span></li>
  </ul>

  <div class="abs side-head" style="top:493px">APPOINTMENT REQUEST</div>
  <div class="abs field" style="top:540px;height:30px">Name (required)</div>
  <div class="abs field" style="top:579px;height:30px">Email (required)</div>
  <div class="abs field" style="top:618px;height:30px">Phone:</div>
  <div class="abs field" style="top:657px;height:137px">Please describe your needs</div>
  <div class="abs submit">Submit</div>
</aside>

<main>
  <div class="abs slider" role="img" aria-label="Photo of a smiling family of four close together"></div>
  <div class="abs slider-caption">Concierge-quality healthcare for your whole family</div>

  <h1 class="abs welcome">Welcome to Larkmoor Medical</h1>
  <p class="abs intro">Lorem ipsum dolor sit amet, consectetur adipiscing elit. Fusce ut ligula et eros molestie ultricies. Ut at elemen tumlacus. Fusce at ligula ante. Nunc non risus eget est feugiat pulvinar. Proin faucibus sem sit amet tortor auctor ac auctor augue tempor. Vestibulum erat velit, aliquam quis conse quat non, convallis nec mi. Vivamus pharetra placerat enim, ut vestibulum lorem iaculis vel. Integer tortor mauris, vulputate vitae accumsan vel, vive.</p>
  <div class="abs video" role="img" aria-label="Video still of a doctor examining a young child"></div>
  <svg class="abs play" viewBox="0 0 42 28"><polygon points="16,7 16,21 28,14" fill="#fff"/></svg>

  <section class="abs pillar" style="left:334px"><h3>— It's about TIME —</h3><p>Lorem ipsum dolor sit amet, co nsectetur adipiscing elit. Fusce ut ligula et eros molestie ultric ies. Ut at elementum lacus sce at ligula ante nunc non risgus.</p><a class="more">LEARN MORE &gt;</a></section>
  <section class="abs pillar" style="left:547px"><h3>— It's about CHOICES —</h3><p>Lorem ipsum dolor sit amet, co nsectetur adipiscing elit. Fusce ut ligula et eros molestie ultric ies. Ut at elementum lacus sce at ligula ante nunc non risgus.</p><a class="more">LEARN MORE &gt;</a></section>
  <section class="abs pillar" style="left:761px"><h3>— It's about YOU —</h3><p>Lorem ipsum dolor sit amet, co nsectetur adipiscing elit. Fusce ut ligula et eros molestie ultric ies. Ut at elementum lacus sce at ligula ante nunc non risgus.</p><a class="more">LEARN MORE &gt;</a></section>
</main>

<a class="abs side-tab" style="top:188px;height:222px">
  <svg width="18" height="22" viewBox="0 0 18 22"><circle cx="9" cy="5" r="4" fill="#fff"/><rect x="7" y="9" width="4" height="8" fill="#fff"/><rect x="2" y="17" width="14" height="3" fill="#fff"/></svg>
  No Appointment? No Problem
</a>
<a class="abs side-tab" style="top:415px;height:135px">
  <svg width="16" height="20" viewBox="0 0 16 20"><rect x="2" y="2" width="12" height="16" rx="1" fill="none" stroke="#fff" stroke-width="2"/></svg>
  Online Checkin
</a>

<footer>
  <div class="abs footer-panel"></div>

  <h2 class="abs foot-head" style="left:111px">LOCATION</h2>
  <div class="abs map" role="img" aria-label="Street map showing the clinic location"></div>
  <p class="abs foot-text" style="left:111px;top:1054px">4120 Larkmoor Ave (at Fairbrook) Ste 180,<br>Dallas, TX 75225</p>
  <div class="abs foot-link" style="left:111px;top:1091px;width:254px">GET DIRECTIONS &gt;<br>USE PUBLIC TRANSPORT &gt;</div>

  <h2 class="abs foot-head" style="left:412px">DOCTOR HOURS</h2>
  <div class="abs hours-photo" role="img" aria-label="Photo of a receptionist wearing a headset"></div>
  <p class="abs foot-text" style="left:412px;top:1054px">Monday – Friday: 9 am to 5 pm<br>Saturday: 9 am to 1 pm</p>
  <div class="abs foot-link" style="left:412px;top:1091px;width:253px">MAKE AN APPOINTMENT &gt;<br>CONTACT US &gt;</div>

  <h2 class="abs foot-head" style="left:712px">LATEST NEWS</h2>
  <ul class="abs news">
    <li>Lorem ipsum dolor sit amet consectet</li>
    <li>Pellentesque porta pretium arcu sit</li>
    <li>Etiam semper ligula non</li>
    <li>Vivamus volutpat sapien non mi solic</li>
    <li>Suspendisse vestibulum eros at eaigm</li>
  </ul>
  <div class="abs foot-link" style="left:712px;top:1062px;width:254px">VIEW ALL NEWS &gt;</div>
  <span class="abs social" style="left:833px;background:#2c5aa6"></span>
  <span class="abs social" style="left:867px;background:#2aa3e0"></span>
  <span class="abs social" style="left:901px;background:#c8231f"></span>
  <span class="abs social" style="left:936px;background:#ee6a1f"></span>

  <nav class="abs bottom-nav">— Home — About — Services — Staff — Insurance — Videos — Contact Us — No Appointment? No Problem — Online Checkin —</nav>
  <p class="abs copyright">©2012 Larkmoor Medical. All Rights Reserved.</p>
</footer>

</body>
</html>
```